Swimming Pool Business Billboard

10' x 24' Billboard displaying company name, logo and phone number. Picture of swimming pool activity; kids playing , swimming, etc. Bullet points possibly shown: New Construction, Repairs, Weekly maintenance.

Industry/Entity Type

Swimming pool construction, repairs and maintenance.

Font styles to use
Sans Serif

Colors
0054AA
0677BA
7BADD7
CADEEF
E8F1F8

Requirements
Must have
• Rusty & Calder Pembrook, RUSTY'S POOLS & Service,
Nice to have
• Prefer to have my last name "Pembrook" above the word "POOLS" only in smaller print so that "RUSTYS POOLS" is distinguished.

```html
<!DOCTYPE html>
<html lang="en">
<head>
<meta charset="utf-8">
<title>Rusty's Pools &amp; Services Billboard</title>
<link rel="stylesheet" href="https://fonts.googleapis.com/css2?family=Bebas+Neue&family=Lato:wght@400;700&display=swap">
<style>
  :root {
    --deep-blue: #0054AA;
    --ocean-blue: #0677BA;
    --sky-blue: #7BADD7;
    --mist-blue: #CADEEF;
    --foam: #E8F1F8;
    --white: #ffffff;
  }
  html, body { margin: 0; padding: 0; overflow: hidden; background: var(--white); }
  .billboard {
    position: relative;
    width: 1200px;
    height: 500px;
    overflow: hidden;
    background: radial-gradient(ellipse at 30% 40%, #1c66b8 0%, var(--deep-blue) 55%, #0a4f9e 100%);
    font-family: 'Lato', sans-serif;
    color: var(--white);
  }
  .wave-art { position: absolute; inset: 0; }
  .brand-name {
    position: absolute;
    left: 29px;
    top: 50px;
    margin: 0;
    font-family: 'Bebas Neue', sans-serif;
    font-weight: 400;
    font-size: 98px;
    line-height: 86px;
    letter-spacing: 1px;
  }
  .family-name {
    position: absolute;
    left: 364px;
    top: 28px;
    font-family: 'Bebas Neue', sans-serif;
    font-size: 30px;
    letter-spacing: 1px;
  }
  .divider {
    position: absolute;
    left: 0;
    top: 243px;
    width: 507px;
    height: 2px;
    background: var(--foam);
  }
  .service-tag {
    position: absolute;
    height: 36px;
    line-height: 36px;
    padding: 0 17px;
    border-radius: 18px;
    background: var(--sky-blue);
    font-size: 27px;
    box-sizing: border-box;
  }
  .tag-construction { left: 26px; top: 273px; }
  .tag-repairs { left: 304px; top: 274px; }
  .tag-maintenance { left: 26px; top: 329px; }
  .phone-icon { position: absolute; left: 12px; top: 412px; }
  .phone-number {
    position: absolute;
    left: 87px;
    top: 392px;
    font-family: 'Bebas Neue', sans-serif;
    font-size: 117px;
    line-height: 100px;
    letter-spacing: 1px;
  }
  .contact-line {
    position: absolute;
    font-size: 29px;
    line-height: 34px;
    white-space: nowrap;
  }
  .contact-email { left: 677px; top: 400px; }
  .contact-address { left: 667px; top: 443px; }
  .contact-icon { position: absolute; }
  .icon-web { left: 634px; top: 405px; }
  .icon-pin { left: 636px; top: 446px; }
  .logo-badge {
    position: absolute;
    left: 607px;
    top: 168px;
    width: 140px;
    height: 140px;
    border-radius: 50%;
    background: var(--white);
    display: flex;
    align-items: center;
    justify-content: center;
    text-align: center;
    color: var(--deep-blue);
    font-family: 'Lato', sans-serif;
    font-weight: 700;
    font-size: 20px;
    line-height: 24px;
  }
</style>
</head>
<body>
<div class="billboard">
  <svg class="wave-art" width="1200" height="500" viewBox="0 0 1200 500">
    <defs>
      <linearGradient id="pool-water" x1="0" y1="0" x2="1" y2="1">
        <stop offset="0" stop-color="#2f5a3a"/>
        <stop offset="0.25" stop-color="#cfe6f2"/>
        <stop offset="0.6" stop-color="#3aa7d6"/>
        <stop offset="1" stop-color="#0b6fa8"/>
      </linearGradient>
    </defs>
    <path class="wave-band" fill="#7BADD7" d="M540 0 C565 40 605 90 600 140 C595 190 515 200 522 260 C530 320 620 330 720 338 C860 350 1020 390 1200 432 L1200 0 Z"/>
    <path class="pool-photo" role="img" aria-label="Photo of a smiling child swimming on a bodyboard in a sparkling pool" fill="url(#pool-water)" d="M600 0 C625 40 645 90 635 140 C625 190 565 210 575 262 C585 312 665 322 765 328 C905 336 1050 352 1200 372 L1200 0 Z"/>
  </svg>

  <div class="family-name">PEMBROOK</div>
  <h1 class="brand-name">RUSTY'S POOLS<br>&amp; SERVICES</h1>
  <div class="divider"></div>

  <div class="service-tag tag-construction">New Construction</div>
  <div class="service-tag tag-repairs">Repairs</div>
  <div class="service-tag tag-maintenance">Weekly Maintenance</div>

  <div class="logo-badge">Rusty's<br>Pools</div>

  <svg class="phone-icon" width="60" height="60" viewBox="0 0 60 60" aria-hidden="true">
    <path fill="#fff" d="M14 6 L22 4 L28 18 L22 23 C25 31 30 37 38 41 L43 35 L56 41 L54 50 C52 55 46 57 40 55 C25 50 11 36 6 21 C4 14 8 8 14 6 Z"/>
    <path fill="none" stroke="#fff" stroke-width="4" stroke-linecap="round" d="M34 12 A14 14 0 0 1 48 26 M34 3 A23 23 0 0 1 57 26 M34 21 A5 5 0 0 1 39 26"/>
  </svg>
  <div class="phone-number">912-555-0147</div>

  <svg class="contact-icon icon-web" width="30" height="30" viewBox="0 0 30 30" aria-hidden="true">
    <g fill="none" stroke="#fff" stroke-width="2">
      <circle cx="15" cy="15" r="13"/>
      <ellipse cx="15" cy="15" rx="6" ry="13"/>
      <path d="M2 15 H28 M4 8 H26 M4 22 H26"/>
    </g>
  </svg>
  <div class="contact-line contact-email">rusty@rcpools.net</div>

  <svg class="contact-icon icon-pin" width="22" height="30" viewBox="0 0 22 30" aria-hidden="true">
    <g fill="none" stroke="#fff" stroke-width="2.2">
      <path d="M11 25 C5 18 3 14 3 10 A8 8 0 0 1 19 10 C19 14 17 18 11 25 Z"/>
      <circle cx="11" cy="10" r="3"/>
      <path d="M5 27 H17"/>
    </g>
  </svg>
  <div class="contact-line contact-address">2750 Marlow Rd Fernbrook, GA 31599</div>
</div>
</body>
</html>
```